Tovrelan Ltda

Logo design focused on: - Construction of civil works - Electrical services - Metal structures - Equipment rental Tomás Ibarra Leiva Manager tovrelan.ltda@brevomail.example 56 9 48215037 Quelitoco s / n, Sorimar, San Pedro de Atacama

Building

Colors
33a6d7
0292cd
33b8a4
0555a3

```html
<!DOCTYPE html>
<html lang="en">
<head>
<meta charset="utf-8">
<title>Tovrelan Ltda – Business Card</title>
<link rel="stylesheet" href="https://fonts.googleapis.com/css2?family=Marcellus&family=PT+Sans:wght@400&display=swap">
<style>
  :root {
    --teal: #1fb5b9;
    --blue: #1470c4;
    --sea: #33b8a4;
    --white: #ffffff;
    --stage: #eef0f2;
    --serif: "Marcellus", Georgia, serif;
    --sans: "PT Sans", Arial, sans-serif;
  }
  * { margin: 0; padding: 0; box-sizing: border-box; }
  html, body { width: 1200px; height: 900px; overflow: hidden; }
  body { background: var(--stage); position: relative; font-family: var(--sans); }

  .card { position: absolute; overflow: hidden; box-shadow: 0 6px 18px rgba(0,0,0,.12); }

  /* Front */
  .card-front { left: 78px; top: 35px; width: 588px; height: 362px; background: var(--teal); color: var(--white); }
  .card-front .backdrop { position: absolute; inset: 0; }
  .contact { position: absolute; left: 28px; top: 36px; z-index: 1; }
  .holder-name { font-family: var(--serif); font-size: 19px; letter-spacing: .5px; text-transform: uppercase; margin-left: 3px; line-height: 22px; }
  .holder-role { font-size: 15px; margin-left: 3px; line-height: 18px; }
  .address { font-size: 15px; line-height: 23px; margin-top: 14px; }
  .lines { margin-top: 12px; font-size: 15px; line-height: 21px; }
  .line { display: flex; align-items: center; gap: 4px; white-space: nowrap; }
  .line svg { flex: none; }
  .line-email { font-size: 13.5px; letter-spacing: -.1px; }
  .services { position: absolute; left: 28px; top: 242px; list-style: none; font-size: 15.5px; line-height: 21.5px; }
  .services li::before { content: ""; display: inline-block; width: 7px; height: 7px; border-radius: 50%; background: var(--white); margin-right: 7px; vertical-align: 2px; }
  .circle-name { position: absolute; left: 275px; top: 155px; width: 300px; text-align: center; font-family: var(--serif); font-size: 34px; color: var(--blue); letter-spacing: 1px; }

  /* Back */
  .card-back { left: 388px; top: 505px; width: 567px; height: 352px; background: var(--white); }
  .brand { position: absolute; left: 88px; top: 145px; display: flex; align-items: center; gap: 14px; }
  .brand-dot { width: 48px; height: 48px; border-radius: 50%; background: var(--blue); }
  .brand-name { font-family: var(--serif); font-size: 40px; color: var(--blue); letter-spacing: 1px; }
</style>
</head>
<body>
  <section class="card card-front" aria-label="Business card, front">
    <svg class="backdrop" width="588" height="362" viewBox="0 0 588 362" aria-hidden="true">
      <rect x="360" y="0" width="228" height="362" fill="var(--blue)"/>
      <circle cx="425" cy="181" r="170" fill="var(--white)"/>
    </svg>
    <div class="contact">
      <p class="holder-name">Tomás Ibarra Leiva</p>
      <p class="holder-role">Director</p>
      <p class="address">Quelitoco s / n, Sorimar,<br>San Pedro de Atacama</p>
      <div class="lines">
        <p class="line">
          <svg width="12" height="12" viewBox="0 0 24 24" aria-hidden="true"><path fill="#fff" d="M6.6 10.8a15 15 0 0 0 6.6 6.6l2.2-2.2a1 1 0 0 1 1-.25 11.4 11.4 0 0 0 3.6.57 1 1 0 0 1 1 1V20a1 1 0 0 1-1 1A17 17 0 0 1 3 4a1 1 0 0 1 1-1h3.5a1 1 0 0 1 1 1c0 1.250.2 2.45.57 3.6a1 1 0 0 1-.25 1z"/></svg>
          <span>56 9 48215037</span>
        </p>
        <p class="line line-email">
          <svg width="12" height="9" viewBox="0 0 24 18" aria-hidden="true"><rect width="24" height="18" rx="1" fill="#fff"/><path d="M1 1l11 9 11-9" fill="none" stroke="var(--teal)" stroke-width="2"/></svg>
          <span>tovrelan.ltda@brevomail.example</span>
        </p>
      </div>
    </div>
    <ul class="services">
      <li>Electrical Services</li>
      <li>Metal Structures</li>
      <li>Equipment Rental</li>
      <li>Construction of Civil Works</li>
    </ul>
    <p class="circle-name">Tovrelan Ltda</p>
  </section>

  <section class="card card-back" aria-label="Business card, back">
    <div class="brand">
      <span class="brand-dot" aria-hidden="true"></span>
      <span class="brand-name">Tovrelan Ltda</span>
    </div>
  </section>
</body>
</html>
```